MD Trailcraft & Wildland Fair

I need a 1 page flyer for promotion of an upcoming sportsman and outdoor show(expo). would like the flyer to be able to be printed in B&W and color! show will include all things to do with the out doors, hunting fishing boating hiking atv camping rvs motorcycles. the event will have a kids zone, events games and activities for kids. there will be vendors showing the newest products. guest speakers and industry experts giving training and advice. this show will have something for everyone. food trucks and concessions. 200+ vendors. waterfould calling competition. deer/buck scoring casting competition for kids 3D Archery competitions

Target Market(s)

anyone event open to all ages!

Colors
ec1f27
000000
fbed22

Requirements
Must have
• date- september 1-2 2018
• location Pelling valley expo 4837 orchardmill rd east calverton MD 21652
• facebook - mdtrailcraftfair
• email mdtrailcraftfair@quorvex.com
• web www.mdtrailcraftfair.com
• vendor spaces still available! sign up now space going fast
Nice to have
• would like some thing that can be both printed in B&W and Color, and still have a great affect.
Should not have
• open to any suggestions

```html
<!DOCTYPE html>
<html lang="en">
<head>
<meta charset="utf-8">
<title>MD Trailcraft &amp; Wildland Fair</title>
<link rel="stylesheet" href="https://fonts.googleapis.com/css2?family=Montserrat:wght@400;600;700;800&family=Raleway:wght@400;500&family=Roboto+Condensed:wght@400&display=swap">
<style>
  :root {
    --red: #b3121c;
    --red-bright: #d4161f;
    --olive: #c4ba3c;
    --olive-dark: #a99f2a;
    --ink: #111111;
    --charcoal: #2a2a2a;
    --paper: #ffffff;
    --teal: #2fa7a0;
    --green: #57b947;
    --navy: #173a52;
  }
  * { box-sizing: border-box; margin: 0; padding: 0; }
  html, body { width: 906px; height: 1200px; overflow: hidden; background: var(--paper); }
  .flyer { position: relative; width: 906px; height: 1200px; background: var(--paper); font-family: "Montserrat", sans-serif; color: var(--ink); }

  .hero-art {
    position: absolute; left: 0; top: 0; width: 906px; height: 643px;
    background:
      radial-gradient(circle at 50% 38%, var(--navy) 0, #1f5f6e 150px, rgba(47,167,160,0.85) 260px, rgba(87,185,71,0.55) 340px, rgba(255,255,255,0) 440px),
      radial-gradient(ellipse at 20% 12%, rgba(87,185,71,0.6), rgba(255,255,255,0) 45%),
      radial-gradient(ellipse at 85% 20%, rgba(47,167,160,0.55), rgba(255,255,255,0) 45%),
      radial-gradient(ellipse at 50% 85%, rgba(60,140,190,0.45), rgba(255,255,255,0) 55%);
  }
  .show-title { position: absolute; left: 0; top: 70px; width: 906px; text-align: center; color: var(--paper); font-weight: 800; line-height: 1; }
  .show-title span { display: block; }
  .show-title .t1 { font-size: 112px; letter-spacing: -2px; }
  .show-title .t2 { font-size: 76px; letter-spacing: -2px; margin-top: 8px; }
  .show-title .t3 { font-size: 58px; letter-spacing: -1px; margin-top: 10px; }

  .floor-space { position: absolute; left: 300px; top: 656px; width: 580px; text-align: center; font-weight: 700; font-size: 19px; line-height: 22px; }
  .floor-space em { font-style: normal; color: var(--red-bright); }

  .date-badge { position: absolute; left: 38px; top: 644px; width: 262px; height: 262px; border-radius: 50%; background: var(--olive); border: 4px solid var(--olive-dark); }
  .date-badge .inner { position: absolute; inset: 0; transform: rotate(-16deg); text-align: center; color: var(--paper); }
  .date-badge .held { position: absolute; top: 42px; left: 0; right: 0; font-family: "Raleway", sans-serif; font-size: 22px; font-weight: 500; }
  .date-badge .month { position: absolute; top: 68px; left: 0; right: 0; font-size: 31px; font-weight: 800; }
  .date-badge .days { position: absolute; top: 98px; left: 0; right: 0; font-size: 108px; font-weight: 800; line-height: 1; }
  .date-badge .days b { color: var(--ink); font-size: 58px; vertical-align: 26px; }
  .date-badge .year { position: absolute; top: 205px; left: 0; right: 0; font-size: 26px; font-weight: 700; letter-spacing: 14px; color: var(--olive-dark); }

  .offerings { position: absolute; left: 346px; top: 722px; display: flex; gap: 0; font-family: "Roboto Condensed", sans-serif; font-size: 17px; list-style: none; }
  .offerings ul { list-style: none; }
  .offerings ul:nth-child(1) { width: 191px; }
  .offerings ul:nth-child(2) { width: 176px; }
  .offerings li { height: 21px; line-height: 21px; display: flex; align-items: center; color: #222; }
  .offerings svg { width: 11px; height: 11px; margin-right: 13px; flex: none; }

  .pitch-band { position: absolute; left: 9px; top: 940px; width: 883px; height: 82px; }
  .pitch-band .tab { position: absolute; top: 0; width: 66px; height: 82px; background: var(--olive); }
  .pitch-band .tab.left { left: 0; }
  .pitch-band .tab.right { right: 0; width: 61px; }
  .pitch { position: absolute; left: 0; top: 940px; width: 906px; text-align: center; }
  .pitch .lead { font-family: "Raleway", sans-serif; font-size: 33px; color: var(--red); line-height: 34px; letter-spacing: 0.5px; }
  .pitch .crowd { font-size: 30px; font-weight: 800; color: var(--red); line-height: 32px; }
  .pitch .expect { font-family: "Raleway", sans-serif; font-size: 19px; color: var(--red); line-height: 24px; margin-top: 3px; }
  .pitch .expect strong { font-family: "Montserrat", sans-serif; font-weight: 800; color: var(--olive-dark); }

  .vendor-call { position: absolute; left: 0; top: 1047px; width: 906px; text-align: center; font-family: "Raleway", sans-serif; font-size: 21px; color: #222; }
  .vendor-call strong { font-family: "Montserrat", sans-serif; font-weight: 800; color: var(--red); font-size: 19px; }

  .contact-bar { position: absolute; left: 11px; top: 1089px; width: 881px; height: 108px; background: var(--charcoal); border-top: 5px solid var(--red); }
  .contact-pill { position: absolute; left: 50%; top: -12px; transform: translateX(-50%); width: 224px; height: 26px; border-radius: 13px; background: var(--olive); border: 2px solid var(--red); text-align: center; font-size: 14px; font-weight: 800; line-height: 22px; color: var(--ink); }
  .contact-lines { position: absolute; left: 0; right: 0; top: 27px; text-align: center; color: var(--paper); font-size: 15.5px; font-weight: 600; line-height: 22px; }
  .contact-lines span { display: inline-flex; align-items: center; margin: 0 6px; }
  .contact-lines svg { width: 12px; height: 12px; margin-right: 8px; }
  .social { position: absolute; right: 24px; bottom: 10px; display: flex; align-items: center; color: var(--paper); font-size: 12px; font-weight: 400; }
  .social i { display: inline-block; width: 11px; height: 11px; border-radius: 50%; background: var(--olive); margin-right: 6px; }
</style>
</head>
<body>
<svg width="0" height="0" style="position:absolute">
  <symbol id="tick-box" viewBox="0 0 12 12">
    <rect x="0.75" y="2.25" width="9" height="9" fill="none" stroke="#b3121c" stroke-width="1.3"/>
    <path d="M2.6 6.4 L5 8.8 L11.2 1.2" fill="none" stroke="#b3121c" stroke-width="1.6"/>
  </symbol>
  <symbol id="pin" viewBox="0 0 12 12"><circle cx="6" cy="6" r="6" fill="#c4ba3c"/><path d="M6 2.5a2.3 2.3 0 0 0-2.3 2.3C3.7 6.6 6 9.5 6 9.5s2.3-2.9 2.3-4.7A2.3 2.3 0 0 0 6 2.5z" fill="#2a2a2a"/></symbol>
  <symbol id="mail" viewBox="0 0 12 12"><circle cx="6" cy="6" r="6" fill="#c4ba3c"/><rect x="3" y="4" width="6" height="4.2" fill="#2a2a2a"/><path d="M3 4 L6 6.4 L9 4" stroke="#c4ba3c" stroke-width="0.8" fill="none"/></symbol>
  <symbol id="globe" viewBox="0 0 12 12"><circle cx="6" cy="6" r="6" fill="#c4ba3c"/><circle cx="6" cy="6" r="3.4" fill="none" stroke="#2a2a2a" stroke-width="0.9"/><path d="M2.6 6h6.8M6 2.6c-1.6 2-1.6 4.8 0 6.8M6 2.6c1.6 2 1.6 4.8 0 6.8" stroke="#2a2a2a" stroke-width="0.8" fill="none"/></symbol>
  <symbol id="phone" viewBox="0 0 12 12"><circle cx="6" cy="6" r="6" fill="#c4ba3c"/><path d="M4 3c.5 0 1 1.2 1 1.5s-.6.6-.5.9c.3.8 1 1.5 1.8 1.8.3.1.6-.5.9-.5s1.5.5 1.5 1S8 9 7.6 9C5.6 9 3 6.4 3 4.4 3 3.9 3.5 3 4 3z" fill="#2a2a2a"/></symbol>
</svg>

<main class="flyer">
  <div class="hero-art" role="img" aria-label="Watercolour collage in greens and teals of outdoor sportsmen: a hiker on a summit, a hunter aiming a shotgun, a dirt bike rider, a couple on a jet ski in splashing water, an archer and an angler casting"></div>

  <h1 class="show-title">
    <span class="t1">MD</span>
    <span class="t2">TRAILCRAFT</span>
    <span class="t3">&amp; WILDLAND FAIR</span>
  </h1>

  <p class="floor-space">Over <em>60,000 sqft of INDOOR and 30,000+ sqft</em><br><em>Outdoor</em> products and services including:</p>

  <div class="date-badge">
    <div class="inner">
      <div class="held">HELD ON</div>
      <div class="month">SEPTEMBER</div>
      <div class="days">1<b>&amp;</b>2</div>
      <div class="year">2018</div>
    </div>
  </div>

  <div class="offerings">
    <ul>
      <li><svg><use href="#tick-box"/></svg>Sports Equipment</li>
      <li><svg><use href="#tick-box"/></svg>Tackle &amp; Bait</li>
      <li><svg><use href="#tick-box"/></svg>Taxidermists</li>
      <li><svg><use href="#tick-box"/></svg>Charter Boats</li>
      <li><svg><use href="#tick-box"/></svg>Trailers</li>
      <li><svg><use href="#tick-box"/></svg>Outdoor Magazines</li>
      <li><svg><use href="#tick-box"/></svg>Camping Equipment</li>
      <li><svg><use href="#tick-box"/></svg>Campers</li>
    </ul>
    <ul>
      <li><svg><use href="#tick-box"/></svg>Motorcycles</li>
      <li><svg><use href="#tick-box"/></svg>Outfitters</li>
      <li><svg><use href="#tick-box"/></svg>Golf Resorts</li>
      <li><svg><use href="#tick-box"/></svg>Sporting Clubs</li>
      <li><svg><use href="#tick-box"/></svg>Camp Grounds</li>
      <li><svg><use href="#tick-box"/></svg>Hunting Supplies</li>
      <li><svg><use href="#tick-box"/></svg>Boats</li>
      <li><svg><use href="#tick-box"/></svg>ATV’s</li>
    </ul>
    <ul>
      <li><svg><use href="#tick-box"/></svg>Guns</li>
      <li><svg><use href="#tick-box"/></svg>Knives</li>
      <li><svg><use href="#tick-box"/></svg>Game Calls</li>
      <li><svg><use href="#tick-box"/></svg>RV’s</li>
      <li><svg><use href="#tick-box"/></svg>Trucks</li>
      <li><svg><use href="#tick-box"/></svg>Jet Skis</li>
      <li><svg><use href="#tick-box"/></svg>Archery</li>
      <li><svg><use href="#tick-box"/></svg>and much more...</li>
    </ul>
  </div>

  <div class="pitch-band"><div class="tab left"></div><div class="tab right"></div></div>
  <section class="pitch">
    <p class="lead">SELL YOUR PRODUCTS AND SERVICES TO</p>
    <p class="crowd">THOUSANDS OF PEOPLE IN ONE WEEKEND!!</p>
    <p class="expect">WE ARE EXPECTING 2 DAY ATTENDANCE TO <strong>TOP 15,000 PEOPLE!</strong></p>
  </section>

  <p class="vendor-call">VENDOR SPACES STILL AVAILABLE! <strong>SIGN UP NOW SPACE GOING FAST</strong></p>

  <footer class="contact-bar">
    <div class="contact-pill">CONTACT US TODAY</div>
    <div class="contact-lines">
      <div><span><svg><use href="#pin"/></svg>Pelling Valley Expo 4837 Orchardmill Rd East Calverton MD 21652</span></div>
      <div><span><svg><use href="#mail"/></svg>mdtrailcraftfair@quorvex.com</span><span><svg><use href="#globe"/></svg>www.mdtrailcraftfair.com</span></div>
      <div><span><svg><use href="#phone"/></svg>410-555-0187 (DANA )</span></div>
    </div>
    <div class="social"><i></i>mdtrailcraftfair</div>
  </footer>
</main>
</body>
</html>
```